Powerpoint visual improvements

I need a cover page, and our beliefs page and differentiating factors page / graphic design for our presentation. For the cover page I would just like an attractive design that incorporate our architectural concept with columns and potentially our logo. For the beliefs page I just want a more attractive presentatoin of the concepts. For the differentiating factors page I want a graphic that captures the points about how we are different from competitors. I have used the attached content to date, but I think it can be improved. The text is included in the graphic and I would also like to make sure the firm logo is incorporated.

Target Market(s)

Individual and institutional investors.

Industry/Entity Type

Investment Advisory

Requirements
Must have
• Our corporate colors are generally RGB 145,148,149; 66,68,76; 0,0,153; and 0,63,127. Our logo is attached. Our primary font is Georgia. Our website is www.PelmarCW.com. The key pages are www.PelmarCW.com/beliefs and www.PelmarCW.com/value we are trying to capture in a presentation. We also need a new presentation cover. Use the website as a reference for the type of imagery we like.

```html
<!DOCTYPE html>
<html lang="en">
<head>
<meta charset="utf-8">
<title>Pelmar – Project Cover</title>
<link href="https://fonts.googleapis.com/css2?family=Gelasio:wght@400&display=swap" rel="stylesheet">
<style>
  :root {
    --navy-deep: #1a3783;
    --navy-mid: #1f4192;
    --navy-soft: #234796;
    --white: #ffffff;
    --motif-light: rgba(255, 255, 255, 0.09);
    --motif-dark: rgba(255, 255, 255, 0.04);
    --tagline: rgba(255, 255, 255, 0.45);
  }
  * { margin: 0; padding: 0; box-sizing: border-box; }
  html, body {
    width: 1200px;
    height: 900px;
    overflow: hidden;
  }
  body {
    font-family: "Gelasio", Georgia, serif;
    color: var(--white);
  }
  .cover {
    position: relative;
    width: 1200px;
    height: 900px;
    overflow: hidden;
    background:
      radial-gradient(ellipse 520px 320px at 260px 560px, rgba(255,255,255,0.05), transparent 70%),
      linear-gradient(160deg, var(--navy-deep) 0%, var(--navy-mid) 55%, var(--navy-soft) 100%);
  }
  .cover__motif {
    position: absolute;
    left: 663px;
    top: 37px;
    width: 840px;
    height: 840px;
    border-radius: 50%;
    background: linear-gradient(90deg, var(--motif-dark) 0%, var(--motif-light) 45%, var(--motif-dark) 100%);
  }
  .brand {
    position: absolute;
    left: 90px;
    top: 285px;
    display: flex;
    align-items: center;
    gap: 12px;
  }
  .brand__dot {
    width: 104px;
    height: 104px;
    border-radius: 50%;
    background: var(--white);
  }
  .brand__text {
    display: flex;
    flex-direction: column;
  }
  .brand__name {
    font-size: 42px;
    line-height: 1;
    font-weight: 400;
    color: var(--white);
  }
  .brand__tagline {
    margin-top: 10px;
    font-size: 9px;
    letter-spacing: 2px;
    color: var(--tagline);
    text-transform: uppercase;
  }
  .headline {
    position: absolute;
    left: 83px;
    top: 426px;
  }
  .headline__title {
    font-size: 48px;
    font-weight: 400;
    line-height: 1.1;
    letter-spacing: 0.5px;
    white-space: nowrap;
  }
  .headline__subtitle {
    margin-top: 10px;
    font-size: 22.5px;
    line-height: 34px;
    max-width: 600px;
  }
</style>
</head>
<body>
  <main class="cover">
    <div class="cover__motif" role="img" aria-label="Faint architectural column motif set within a large circle"></div>

    <div class="brand">
      <span class="brand__dot"></span>
      <div class="brand__text">
        <span class="brand__name">Pelmar</span>
        <span class="brand__tagline">Capital Wealth</span>
      </div>
    </div>

    <section class="headline">
      <h1 class="headline__title">PROJECT TITLE HERE</h1>
      <p class="headline__subtitle">Subtext here Subtext here Subtext here Subtext here Subtext here Subtext here Subtext here</p>
    </section>
  </main>
</body>
</html>
```